freelance Nursing care

I'm starting my business as a freelance nurse. With this flyer, i would like to introduce my practice to the doctore as well as to the patients.<br/>my specialization is urodynamics and pelviperineology. i will be working as a consutant in my office and also in home care.<br/><br/>can you make a design with my logo and introduce my description in the flyer.

Target Market(s)

Doctor and patients

Industry/Entity Type

Health Care

Colors

Designer to choose colors to be used in the design.

Requirements
Must have
• - office and home cares services ( see in attache files). you can find it in Offre en soins en cabinet et à domicile
• - Advantage
• - training ( formation)
• -personal coordinate ( coordonnée personnelle)
• -Logo
Nice to have
• attractive design

```html
<!DOCTYPE html>
<html lang="fr">
<head>
<meta charset="utf-8">
<title>Laverne Soins – Flyer</title>
<link href="https://fonts.googleapis.com/css2?family=Bebas+Neue&family=Open+Sans:wght@400;600&display=swap" rel="stylesheet">
<style>
  :root{
    --page-bg:#e4e4e4;
    --teal:#178f9c;
    --blue-deep:#1584b4;
    --blue-mid:#1a9cc8;
    --panel-teal:#17a5c6;
    --photo-bg:#1488c4;
    --photo-light:#5cb4ea;
    --photo-mid:#2aa0dc;
    --ink:#1d1d1d;
    --white:#ffffff;
  }
  *{box-sizing:border-box;margin:0;padding:0}
  html,body{width:1200px;height:2971px;overflow:hidden;background:var(--page-bg)}
  .flyer{
    position:absolute;left:80px;top:745px;width:1040px;height:1471px;
    background:var(--white);overflow:hidden;
    box-shadow:0 6px 18px rgba(0,0,0,.25);
    font-family:'Open Sans',sans-serif;color:var(--ink);
  }
  .hero{position:absolute;left:0;top:0;width:1040px;height:685px;background:var(--blue-deep)}
  .hero-photo{
    position:absolute;left:424px;top:0;width:616px;height:600px;
    background:
      radial-gradient(ellipse 200px 260px at 58% 62%, var(--photo-light) 0%, rgba(92,180,234,0) 100%),
      radial-gradient(ellipse 90px 110px at 60% 26%, var(--photo-mid) 0%, rgba(42,160,220,0) 100%),
      linear-gradient(135deg, #0f74ac 0%, var(--photo-bg) 45%, #1da0d8 100%);
  }
  .title-panel{position:absolute;left:0;top:0;width:424px;height:470px;background:var(--white)}
  .brand{
    position:absolute;left:36px;top:56px;display:flex;align-items:center;gap:10px;
    font-weight:600;font-size:26px;color:var(--teal);
  }
  .brand-dot{width:16px;height:16px;border-radius:50%;background:var(--teal)}
  .headline{
    position:absolute;left:28px;top:160px;
    font-family:'Bebas Neue',sans-serif;font-weight:400;font-size:92px;line-height:.84;color:var(--teal);
  }
  .waves{position:absolute;left:0;top:380px;width:1040px;height:305px}
  .lower{position:absolute;left:0;top:685px;width:1040px;height:786px}
  .services{position:absolute;left:0;top:0;width:543px;height:786px;background:var(--white);padding:50px 68px 0 56px}
  .benefits{position:absolute;left:543px;top:0;width:497px;height:786px;background:var(--panel-teal);padding:40px 24px 0 40px;color:var(--white)}
  .section-title{font-family:'Bebas Neue',sans-serif;font-weight:400;font-size:48px;line-height:.95;color:var(--blue-mid)}
  .panel-title{font-family:'Bebas Neue',sans-serif;font-weight:400;font-size:115px;line-height:.9;color:var(--white)}
  .checklist{list-style:none;margin-top:28px}
  .checklist li{position:relative;padding-left:24px;font-size:15.5px;line-height:1.12;margin-bottom:10px}
  .checklist li::before{
    content:"";position:absolute;left:5px;top:2px;width:6px;height:12px;
    border:solid currentColor;border-width:0 3px 3px 0;transform:rotate(40deg);
  }
  .benefits .checklist{margin:24px 0 20px}
  .benefits .formation-list{margin-top:24px}
  .contact{margin-top:36px}
  .contact-address{font-size:15.5px;line-height:1.1;margin:8px 0 12px 26px}
  .contact-line{display:flex;align-items:center;gap:8px;font-family:'Bebas Neue',sans-serif;font-size:46px;line-height:1.12;color:var(--blue-mid)}
  .contact-line svg{flex:none}
</style>
</head>
<body>
<main class="flyer">
  <section class="hero">
    <div class="hero-photo" role="img" aria-label="Photo d'une infirmière en blouse et charlotte bleues tenant un stéthoscope"></div>
    <div class="title-panel">
      <div class="brand"><span class="brand-dot"></span>Laverne Soins</div>
      <h1 class="headline">Votre santé<br>est<br>importante</h1>
    </div>
    <svg class="waves" viewBox="0 0 1040 305" preserveAspectRatio="none" aria-hidden="true">
      <path d="M0 90 C180 10 380 10 560 70 C720 125 880 150 1040 110 L1040 305 L0 305Z" fill="#38bfee"/>
      <path d="M0 130 C200 40 400 50 580 110 C740 160 900 175 1040 140 L1040 305 L0 305Z" fill="#ffffff"/>
      <path d="M0 145 C200 60 400 70 580 128 C740 178 900 192 1040 160 L1040 305 L0 305Z" fill="#2fd4ff"/>
      <path d="M0 190 C220 100 420 110 600 170 C760 218 910 225 1040 200 L1040 305 L0 305Z" fill="#1584b4"/>
    </svg>
  </section>

  <section class="lower">
    <div class="services">
      <h2 class="section-title">Offre en soins en<br>cabinet et à domicile</h2>
      <ul class="checklist">
        <li>Enseignement en soins d’incontinence<br>(condoms, tampons, irrigation anale,<br>protection…etc.)</li>
        <li>Enseignement à l’auto-sondage</li>
        <li>Changement de sonde sus pubien<br>ou transurétrale</li>
        <li>Enseignement de neurostimulation tibiale,<br>intravaginale, vagale.</li>
        <li>Dilatations par hétéro-sondage</li>
        <li>Pansements etc</li>
        <li>Sous Mandat : Effectuer le bilan urodynamique<br>(BUD) en collaboration avec médecin spécialiste.</li>
        <li>Pose de sonde nasogastrique, pose VVP, PAC,<br>perfusion des ATB etc…</li>
        <li>Contrôle de santé, préparation de semainier</li>
      </ul>
      <div class="contact">
        <h2 class="section-title">Coordonnées personnelles</h2>
        <p class="contact-address">Cabinet des Tilleuls, Rue des Vergers 14<br>2300 Valmont</p>
        <p class="contact-line">
          <svg width="26" height="22" viewBox="0 0 26 22" aria-hidden="true"><path d="M2 7 C2 2 24 2 24 7 L20 9 L18 6 L8 6 L6 9Z M6 11 L20 11 L22 20 L4 20Z" fill="#1a9cc8"/><circle cx="13" cy="15" r="3" fill="#fff"/></svg>
          079 418 26 53
        </p>
        <p class="contact-line">
          <svg width="26" height="18" viewBox="0 0 26 18" aria-hidden="true"><rect x="1" y="1" width="24" height="16" fill="#1a9cc8"/><path d="M1 1 L13 10 L25 1" stroke="#fff" stroke-width="2" fill="none"/></svg>
          soins@laverne.ch
        </p>
      </div>
    </div>

    <div class="benefits">
      <h2 class="panel-title">Avantages</h2>
      <ul class="checklist">
        <li>Offrir un suivi personnalisé et de qualité à chaque<br>besoin, avec la même intervenante ayant une<br>expertise du domaine de compétence.</li>
        <li>Promouvoir la plus grande autonomie et la<br>meilleure qualité de vie</li>
        <li>Conseils et promotion de la santé</li>
        <li>Intégrer le plus rapidement possible le domicile<br>après une hospitalisation</li>
        <li>Contribuer au développement de réseaux de soin.</li>
      </ul>
      <h2 class="panel-title">Formation</h2>
      <ul class="checklist formation-list">
        <li>Participation aux divers congrès d’urologie (SEUP,<br>ALPU, CORA, Symposium de Neuro urologie CHUR)</li>
        <li>Diplôme université d’urodynamique et pelvi-<br>périnéologie</li>
        <li>Expériences divers (Oncologie, Gynécologie,<br>Urodynamique et pelvi-périnéologie)</li>
        <li>Infirmière HES depuis 10 ans</li>
      </ul>
    </div>
  </section>
</main>
</body>
</html>
```